GUARANTEED! Simple website for independent event planner and consultant...

I need a website that is no more than 5 or 6 pages to illustrate who I am and what I can offer to groups who book hotels for meetings and conferences. I have 20 years of experience planning meetings within hotels and I am now ready to go out on my own and help clients choose venues, negotiate contracts and plan effective meetings. I will focus on clients planning meetings in the mountains of Colorado but I am willing to travel as well. I want to work with a person who is collaborative and can direct me on what they need to move the project along quickly. I already have my logo, a hosting site and work e-mail address. Also, I recently hired a photographer to do head shots. Lastly, it important for me to be able to talk on the phone or skype with this person, as needed and I must be able to make changes to my site down the road when necessary...

Target Market(s)

Corporate Groups

Industry/Entity Type

Event Planning

Coding

Coded - Design and coding required

Number of Pages Required

5+ page

Font styles to use
Sans Serif

Requirements
Must have
• About me page, event planning services offered page, task force and consulting work page, testimonials page, page for blogs, page to contact me/request a proposal. May need advice on what else I need...
Nice to have
• I want it to look sharp and professional. I want people to look at my site and know immediately that they can trust me and the work I can do.
• I don't want it to look like it is over the top as I am not a HUGE company but I do want it to be professional and easy to view and navigate.
Should not have
• Bright colors
• My logo is bright orange and black. I have also used dark grey and orange. See below:
• Orange:
• C = 0
• M = 64
• Y = 100
• K = 0
• Gray:
• C = 67
• M = 60
• Y = 59
• K = 45
• Font: Gotham Book and Gotham Bold

```html
<!DOCTYPE html>
<html lang="en">
<head>
<meta charset="utf-8">
<title>Dana Whitfield — Event Planner and Consultant</title>
<link rel="stylesheet" href="https://fonts.googleapis.com/css2?family=Montserrat:wght@400;500;600;700;800&display=swap">
<style>
:root{
  --orange:#f5821f;
  --orange-deep:#e6731a;
  --charcoal:#3a3a3a;
  --ink:#222;
  --dark:#1c1c1c;
  --grey-bg:#eeeeee;
  --grey-card:#e2e2e2;
  --grey-line:#cfcfcf;
  --text:#555;
  --white:#fff;
}
*{margin:0;padding:0;box-sizing:border-box}
html,body{width:1200px;height:5325px;overflow:hidden}
body{font-family:"Montserrat",sans-serif;color:var(--text);background:var(--white);position:relative}
.section{position:absolute;left:0;width:1200px}
.abs{position:absolute}
.photo{position:absolute}
.section-title{position:absolute;font-weight:700;font-size:24px;color:var(--ink);letter-spacing:1px}
.section-title .dash{color:var(--orange)}

/* header */
.site-header{top:0;height:107px;background:var(--white)}
.brand{position:absolute;left:0;width:1200px;top:34px;text-align:center}
.brand-name{font-weight:600;font-size:26px;color:var(--charcoal);letter-spacing:3px}
.main-nav{top:107px;height:53px;background:linear-gradient(#f4f4f4,#dcdcdc);border-bottom:1px solid #c8c8c8;display:flex;align-items:center;padding-left:60px}
.main-nav a{font-size:14px;color:#444;text-decoration:none;font-weight:500;margin-right:56px}

/* hero */
.hero{top:160px;height:780px;background:var(--dark)}
.hero .photo{left:520px;top:0;width:680px;height:780px;background:radial-gradient(ellipse at 55% 40%,#7a7a7a 0%,#3c3c3c 45%,#1c1c1c 80%)}
.hero-greeting{left:88px;top:200px;font-size:46px;color:var(--white);font-weight:500;letter-spacing:1px}
.hero-name{left:88px;top:255px;font-size:80px;line-height:78px;color:var(--orange);font-weight:800;letter-spacing:2px}
.hero-role{left:90px;top:430px;font-size:18px;color:var(--white);letter-spacing:1px}
.social{left:90px;top:480px;display:flex;gap:14px}
.social span{width:42px;height:42px;border-radius:50%;background:#e8e8e8}

/* about */
.about{top:940px;height:605px;background:var(--grey-bg)}
.about .photo{left:560px;top:20px;width:460px;height:585px;background:linear-gradient(180deg,#d9d5d0,#b7afa8 60%,#6d6661)}
.about .section-title{left:100px;top:95px}
.about-intro{left:100px;top:150px;width:440px;font-size:14px;line-height:22px}
.about-facts{left:100px;top:230px;width:440px;font-size:14px}
.about-facts li{list-style:none;padding:13px 0;border-bottom:1px solid var(--grey-line)}
.about-facts b{color:var(--ink)}
.btn-dark{left:100px;top:482px;background:var(--charcoal);color:var(--white);font-size:13px;font-weight:700;padding:12px 18px}
.scroll-tab{left:560px;width:80px;height:40px;border-radius:80px 80px 0 0;background:var(--white)}

/* event planning */
.planning{top:1545px;height:530px}
.planning .section-title{left:100px;top:95px}
.service{width:320px}
.service svg{position:absolute;left:0;top:0}
.service h3{position:absolute;left:60px;top:0;font-size:15px;color:var(--orange);font-weight:700}
.service p{position:absolute;left:60px;top:26px;width:250px;font-size:12px;line-height:18px}
.service .rule{position:absolute;left:60px;top:90px;width:250px;border-top:1px solid var(--grey-line)}

/* stats */
.stats{top:2077px;height:235px;display:flex}
.stat{width:300px;height:235px;background:var(--orange);color:var(--white);text-align:center;padding-top:40px}
.stat:nth-child(even){background:var(--orange-deep)}
.stat b{display:block;font-size:36px;font-weight:700}
.stat small{display:block;font-size:17px;font-weight:700;margin-top:4px}
.stat svg{margin-top:22px}

/* task force */
.taskforce{top:2312px;height:665px}
.taskforce .photo{left:0;top:0;width:480px;height:665px;background:linear-gradient(90deg,#d8d3cf,#bdb3ab 50%,#efefef)}
.taskforce .section-title{left:520px;top:70px}
.tf-intro{left:520px;top:115px;width:640px;font-size:15px;line-height:22px;color:var(--orange)}
.tf-item{width:300px}
.tf-item .num{position:absolute;left:0;top:0;font-size:30px;font-weight:700;color:var(--orange)}
.tf-item h4{position:absolute;left:70px;top:2px;font-size:15px;color:var(--ink)}
.tf-item p{position:absolute;left:70px;top:26px;font-size:11px;color:#888;width:220px;line-height:15px}
.tf-item .rule{position:absolute;left:0;top:-16px;width:300px;border-top:1px solid var(--grey-line)}
.tf-quote{left:520px;top:540px;width:620px;font-size:16px;line-height:22px;color:var(--orange);padding-left:70px}
.tf-quote .mark{position:absolute;left:0;top:-6px;font-size:70px;line-height:60px;font-weight:800}

/* consulting */
.consulting{top:2975px;height:345px}
.consulting .section-title{left:100px;top:60px}
.consult{width:230px;top:125px}
.consult h3{font-size:16px;color:var(--ink);font-weight:700}
.consult .role{font-size:10px;color:var(--orange);letter-spacing:1px;padding-bottom:10px;border-bottom:3px solid var(--orange)}
.consult p{font-size:12px;line-height:18px;margin-top:14px}

/* testimonials */
.testimonials{top:3320px;height:500px;background:var(--grey-bg)}
.testimonials .section-title{left:0;width:1200px;text-align:center;top:60px}
.t-sub{left:0;width:1200px;text-align:center;top:100px;font-size:14px;color:#444;letter-spacing:2px}
.t-card{width:300px;top:165px;height:185px;background:var(--grey-card);padding:28px 30px;font-size:13px;line-height:20px;color:#666}
.t-person{top:385px;display:flex;align-items:center;gap:14px}
.avatar{width:56px;height:56px;border-radius:50%;background:linear-gradient(#a59a90,#6a625c)}
.t-person b{display:block;font-size:14px;color:var(--ink)}
.t-person small{font-size:12px;color:#777}

/* blog */
.blog{top:3820px;height:700px}
.blog .section-title{left:100px;top:40px}
.post{width:292px;height:300px;background:var(--white);padding:40px 30px;color:var(--ink)}
.post .q{font-size:60px;line-height:40px;font-weight:800;color:var(--orange)}
.post h3{font-size:15px;line-height:22px;font-weight:700;margin-top:16px}
.post .date{font-size:11px;margin-top:20px;color:#777}
.post .by{font-size:11px;font-weight:700;margin-top:6px;color:#555}
.post.dark{background:var(--charcoal);color:var(--white);outline:3px solid var(--white);outline-offset:-18px}
.post.dark .date,.post.dark .by{color:var(--white)}
.post.accent{background:var(--orange);color:var(--white);outline:3px solid var(--white);outline-offset:-18px}
.post.accent .q,.post.accent .date,.post.accent .by{color:var(--white)}
.post.framed{border:4px solid #bdbdbd}

/* contact */
.contact{top:4520px;height:600px;background:linear-gradient(90deg,#ebebe8,#f3f3f0)}
.contact .photo{left:640px;top:0;width:560px;height:600px;background:radial-gradient(ellipse at 55% 45%,#cfcfcb,#ecece9 70%)}
.contact .section-title{left:100px;top:100px}
.c-info{top:175px;display:flex;gap:12px;font-size:11px;line-height:15px;color:#666}
.field{left:100px;width:440px;border-bottom:1px solid var(--grey-line);font-size:12px;color:#777;padding-bottom:12px}
.btn-submit{left:100px;top:505px;background:var(--orange-deep);color:var(--white);font-size:12px;font-weight:700;padding:9px 18px}

/* footer */
.site-footer{top:5120px;height:205px;background:var(--dark)}
.copyright{left:100px;top:92px;font-size:12px;color:#aaa}
.footer-brand{left:900px;top:84px;width:200px;text-align:right}
.footer-brand .brand-name{font-size:20px;color:#cfcfcf}
.up-tab{left:565px;top:-22px;width:70px;height:44px;border-radius:70px 70px 0 0;background:var(--dark)}
</style>
</head>
<body>

<header class="section site-header">
  <div class="brand"><span class="brand-name">RIDGELINE</span></div>
</header>
<nav class="section main-nav">
  <a>ABOUT ME</a><a>EVENT PLANNING</a><a>TASK FORCE</a><a>CONSULTING</a><a>TESTIMONIALS</a><a>BLOGS</a><a>CONTACT ME</a>
</nav>

<section class="section hero">
  <div class="photo" role="img" aria-label="Black and white portrait of the event planner smiling, hand at her chin"></div>
  <div class="abs hero-greeting">HELLO I'M</div>
  <h1 class="abs hero-name">DANA<br>WHITFIELD</h1>
  <div class="abs hero-role">EVENT PLANNER AND CONSULTANT</div>
  <div class="abs social"><span></span><span></span><span></span><span></span></div>
</section>

<section class="section about">
  <div class="photo" role="img" aria-label="Portrait of the event planner in a dark blazer"></div>
  <h2 class="section-title"><span class="dash">-</span> ABOUT ME <span class="dash">-</span></h2>
  <p class="abs about-intro">Hello, I'm Event planner and Consultant I hold a master degree of Web Design from the World University.</p>
  <ul class="abs about-facts">
    <li><b>Name:</b> Dana Whitfield</li>
    <li><b>Email:</b> dana@ridgeline-events.com</li>
    <li><b>Phone:</b> (555) 014-2290</li>
    <li><b>Date of birth:</b> 23 February 1986</li>
    <li><b>Nationality:</b> United States</li>
  </ul>
  <div class="abs btn-dark">DOWNLOAD RESUME</div>
  <div class="abs scroll-tab" style="top:565px"><svg width="80" height="40"><polyline points="33,18 40,25 47,18" fill="none" stroke="#999" stroke-width="2"/></svg></div>
</section>

<section class="section planning">
  <h2 class="section-title"><span class="dash">-</span> EVENT PLANNING <span class="dash">-</span></h2>

  <div class="abs service" style="left:100px;top:200px">
    <svg width="44" height="40" fill="none" stroke="#f5821f" stroke-width="2"><rect x="3" y="8" width="38" height="28"/><line x1="3" y1="16" x2="41" y2="16"/><line x1="12" y1="3" x2="12" y2="12"/><line x1="32" y1="3" x2="32" y2="12"/></svg>
    <h3>HEADING 1</h3><p>Plan each meeting with clear goals, fitting rooms and a steady schedule for your group.</p><span class="rule"></span>
  </div>
  <div class="abs service" style="left:460px;top:200px">
    <svg width="44" height="40" fill="none" stroke="#f5821f" stroke-width="2"><rect x="4" y="6" width="36" height="22"/><line x1="22" y1="28" x2="22" y2="38"/><line x1="12" y1="38" x2="32" y2="38"/></svg>
    <h3>HEADING 2</h3><p>Select venues that suit your budget, your attendees and the purpose of the event.</p><span class="rule"></span>
  </div>
  <div class="abs service" style="left:810px;top:200px">
    <svg width="44" height="40" fill="none" stroke="#f5821f" stroke-width="2"><circle cx="22" cy="12" r="8"/><path d="M6 38c0-10 8-16 16-16s16 6 16 16"/></svg>
    <h3>HEADING 3</h3><p>Guide speakers and guests so every session starts on time and runs smoothly.</p><span class="rule"></span>
  </div>
  <div class="abs service" style="left:100px;top:345px">
    <svg width="44" height="40" fill="none" stroke="#f5821f" stroke-width="2"><rect x="4" y="14" width="36" height="14"/><line x1="8" y1="28" x2="8" y2="38"/><line x1="36" y1="28" x2="36" y2="38"/></svg>
    <h3>HEADING 4</h3><p>Arrange seating, catering and room layouts that keep attendees focused and comfortable.</p><span class="rule"></span>
  </div>
  <div class="abs service" style="left:460px;top:345px">
    <svg width="44" height="40" fill="none" stroke="#f5821f" stroke-width="2"><rect x="6" y="4" width="32" height="34"/><line x1="12" y1="14" x2="32" y2="14"/><line x1="12" y1="22" x2="32" y2="22"/><line x1="12" y1="30" x2="26" y2="30"/></svg>
    <h3>HEADING 5</h3><p>Review hotel contracts line by line and negotiate terms that protect your group.</p><span class="rule"></span>
  </div>
  <div class="abs service" style="left:810px;top:345px">
    <svg width="44" height="40" fill="none" stroke="#f5821f" stroke-width="2"><circle cx="14" cy="14" r="7"/><circle cx="30" cy="14" r="7"/><path d="M2 38c0-8 5-13 12-13s12 5 12 13M18 38c0-8 5-13 12-13s12 5 12 13"/></svg>
    <h3>HEADING 6</h3><p>Coordinate teams on site so problems are solved quietly before guests notice.</p><span class="rule"></span>
  </div>
</section>

<section class="section stats">
  <div class="stat"><b>140</b><small>SPEAKERS</small><svg width="50" height="50" fill="none" stroke="#fff" stroke-width="2"><circle cx="16" cy="12" r="6"/><path d="M6 44V28c0-5 4-8 10-8s10 3 10 8v16"/><rect x="30" y="6" width="16" height="12"/></svg></div>
  <div class="stat"><b>7</b><small>DAYS EVENT</small><svg width="50" height="50" fill="none" stroke="#fff" stroke-width="2"><rect x="6" y="10" width="38" height="34"/><line x1="6" y1="20" x2="44" y2="20"/><line x1="15" y1="4" x2="15" y2="14"/><line x1="35" y1="4" x2="35" y2="14"/></svg></div>
  <div class="stat"><b>20</b><small>WORKSHOPS</small><svg width="50" height="50" fill="none" stroke="#fff" stroke-width="2"><rect x="5" y="16" width="40" height="28"/><path d="M18 16v-6h14v6"/><line x1="5" y1="28" x2="45" y2="28"/></svg></div>
  <div class="stat"><b>395</b><small>MEMBER REGISTERED</small><svg width="50" height="50" fill="none" stroke="#fff" stroke-width="2"><rect x="8" y="6" width="30" height="38"/><line x1="14" y1="16" x2="32" y2="16"/><line x1="14" y1="24" x2="32" y2="24"/><line x1="14" y1="32" x2="26" y2="32"/><line x1="44" y1="12" x2="30" y2="40"/></svg></div>
</section>

<section class="section taskforce">
  <div class="photo" role="img" aria-label="Portrait of the event planner in a light cardigan, smiling"></div>
  <h2 class="section-title"><span class="dash">-</span> TASK FORCE <span class="dash">-</span></h2>
  <p class="abs tf-intro">Lorem Ipsum is simply dummy text of the printing and typesetting industry. Lorem Ipsum has been the industry's standard dummy text ever since the 1500s.</p>
  <div class="abs tf-item" style="left:520px;top:245px"><span class="rule"></span><span class="num">01</span><h4>LOREM IPSUM DOLOR</h4><p>SET GOALS AND TIMELINES FOR EACH TEAM</p></div>
  <div class="abs tf-item" style="left:860px;top:245px"><span class="rule"></span><span class="num">02</span><h4>LOREM IPSUM DOLOR</h4><p>ASSIGN ROLES AND SHARE CLEAR TASKS</p></div>
  <div class="abs tf-item" style="left:520px;top:350px"><span class="rule"></span><span class="num">03</span><h4>LOREM IPSUM DOLOR</h4><p>TRACK PROGRESS WITH WEEKLY CHECK INS</p></div>
  <div class="abs tf-item" style="left:860px;top:350px"><span class="rule"></span><span class="num">04</span><h4>LOREM IPSUM DOLOR</h4><p>REVIEW RESULTS AFTER EVERY EVENT DAY</p></div>
  <p class="abs tf-quote"><span class="mark">“</span>LOREM IPSUM DOLOR SIT AMET, CONSECTETUR ADIPISCING ELIT, SED DO EIUSMOD TEMPOR.</p>
</section>

<section class="section consulting">
  <h2 class="section-title"><span class="dash">-</span> CONSULTING <span class="dash">-</span></h2>
  <div class="abs consult" style="left:100px"><h3>HEADING 1</h3><div class="role">DESIGNATION</div><p>Practical advice on venues, budgets and timelines shaped around your group's needs.</p></div>
  <div class="abs consult" style="left:365px"><h3>HEADING 2</h3><div class="role">DESIGNATION</div><p>Clear guidance on contract terms, room blocks and attrition before you sign.</p></div>
  <div class="abs consult" style="left:630px"><h3>HEADING 3</h3><div class="role">DESIGNATION</div><p>Honest reviews of past meetings with simple steps to improve the next one.</p></div>
  <div class="abs consult" style="left:895px"><h3>HEADING 4</h3><div class="role">DESIGNATION</div><p>Support for mountain destinations in Colorado and travel to venues elsewhere.</p></div>
</section>

<section class="section testimonials">
  <h2 class="section-title"><span class="dash">-</span> TESTIMONIALS <span class="dash">-</span></h2>
  <div class="abs t-sub">WHAT PEOPLE SAY</div>
  <div class="abs t-card" style="left:100px">Dana found our venue, handled every contract detail and kept our whole team calm. Our conference ran better than any year before.</div>
  <div class="abs t-card" style="left:450px">Working with Dana was easy. She listened, planned ahead and solved small problems before they reached our guests at the event.</div>
  <div class="abs t-card" style="left:800px">Her knowledge of mountain hotels saved us time and money. We will book our next annual meeting with her without a doubt.</div>
  <div class="abs t-person" style="left:100px"><span class="avatar" role="img" aria-label="Client portrait"></span><div><b>SAM PORTER</b><small>Project Manager</small></div></div>
  <div class="abs t-person" style="left:450px"><span class="avatar" role="img" aria-label="Client portrait"></span><div><b>SAM PORTER</b><small>Project Manager</small></div></div>
  <div class="abs t-person" style="left:800px"><span class="avatar" role="img" aria-label="Client portrait"></span><div><b>SAM PORTER</b><small>Project Manager</small></div></div>
</section>

<section class="section blog">
  <h2 class="section-title"><span class="dash">-</span> RECENT BLOG <span class="dash">-</span></h2>
  <article class="abs post dark" style="left:106px;top:103px"><div class="q">“</div><h3>A PORTRAIT IS NOT MADE IN THE CAMERA BUT ON EITHER SIDE OF IT.</h3><div class="date">APRIL 11, 2016</div><div class="by">POSTED BY ADMIN</div></article>
  <article class="abs post" style="left:444px;top:103px"><div class="q">“</div><h3>A PORTRAIT IS NOT MADE IN THE CAMERA BUT ON EITHER SIDE OF IT.</h3><div class="date">APRIL 11, 2016</div><div class="by">POSTED BY ADMIN</div></article>
  <article class="abs post framed" style="left:781px;top:103px"><div class="q">“</div><h3>A PORTRAIT IS NOT MADE IN THE CAMERA BUT ON EITHER SIDE OF IT.</h3><div class="date">APRIL 11, 2016</div><div class="by">POSTED BY ADMIN</div></article>
  <article class="abs post" style="left:106px;top:420px"><div class="q">“</div><h3>A PORTRAIT IS NOT MADE IN THE CAMERA BUT ON EITHER SIDE OF IT.</h3><div class="date">APRIL 11, 2016</div><div class="by">POSTED BY ADMIN</div></article>
  <article class="abs post accent" style="left:444px;top:400px"><div class="q">“</div><h3>A PORTRAIT IS NOT MADE IN THE CAMERA BUT ON EITHER SIDE OF IT.</h3><div class="date">APRIL 11, 2016</div><div class="by">POSTED BY ADMIN</div></article>
  <article class="abs post" style="left:781px;top:420px"><div class="q">“</div><h3>A PORTRAIT IS NOT MADE IN THE CAMERA BUT ON EITHER SIDE OF IT.</h3><div class="date">APRIL 11, 2016</div><div class="by">POSTED BY ADMIN</div></article>
</section>

<section class="section contact">
  <div class="photo" role="img" aria-label="Pencil-style portrait of the event planner, arms folded"></div>
  <h2 class="section-title"><span class="dash">-</span> CONTACT ME <span class="dash">-</span></h2>
  <div class="abs c-info" style="left:100px"><svg width="24" height="28" fill="none" stroke="#999" stroke-width="2"><path d="M12 26s9-9 9-15a9 9 0 0 0-18 0c0 6 9 15 9 15z"/><circle cx="12" cy="11" r="3"/></svg><span>LOREM IPSUM DOLOR SIT<br>CONSECTETUR</span></div>
  <div class="abs c-info" style="left:340px"><svg width="28" height="22" fill="none" stroke="#999" stroke-width="2"><rect x="2" y="3" width="24" height="16"/><polyline points="2,3 14,12 26,3"/></svg><span>GENERAL ENQUIRIES<br>hello@ridgeline-events.com</span></div>
  <div class="abs field" style="top:248px">YOUR NAME*</div>
  <div class="abs field" style="top:305px">YOUR EMAIL*</div>
  <div class="abs field" style="top:362px">WHAT ARE YOU INTERESTED IN?</div>
  <div class="abs field" style="top:419px;padding-bottom:40px">YOUR MESSAGE</div>
  <div class="abs btn-submit">SUBMIT</div>
</section>

<footer class="section site-footer">
  <div class="abs up-tab"><svg width="70" height="44"><polyline points="28,26 35,19 42,26" fill="none" stroke="#999" stroke-width="2"/></svg></div>
  <div class="abs copyright">© 2017 RIDGELINE EVENT MANAGEMENT. ALL RIGHTS RESERVED 2016</div>
  <div class="abs footer-brand"><span class="brand-name">RIDGELINE</span></div>
</footer>

</body>
</html>
```